New Custom Pizza Box Design Project For Independant Restaurant

We are looking for creative designs for our new custom printed pizza boxes. Designs should include the following:

-Our logo & company name
-A color scheme similar to our current logo
-Our physical and URL addresses & phone number (menu is attached)
-Ability to scale the design across several box sizes (10x10x2, 14x14x2, 18x13x2,
26x18x2)
- Any creative flair you think will make for the best design

Design can be on a white or kraft (tan) box.
Designs can be either two or three ink colors.

***Please note, designs must be able to be screen printed on boxes***
Updates

Reason: Still debating which to choose

Target Market(s)

Industry/Entity Type

Pizza Delivery

Font styles to use
Other font styles liked:
• Please use font similar to our logo text

Requirements
Must have
• -2 or 3 ink colors
• -company name, address, phone number, URL
• -company logo and colors
• -flexibility to use on different box sizes (10x10x2, 14x14x2, 18x13x2,
• 26x18x2)
• -utilize full printable area on boxes (including 2" dimension on box sides)
• ***Please note, designs must be able to be screen printed on boxes***
Should not have
• Design features with strong similarities to existing designs of other pizzerias

```html
<!DOCTYPE html>
<html lang="en">
<head>
<meta charset="utf-8">
<title>Marlow's Finchyard Pizzeria – Pizza Box Lid</title>
<link rel="stylesheet" href="https://fonts.googleapis.com/css2?family=Archivo+Black&family=Roboto+Condensed:wght@700&display=swap">
<style>
  :root {
    --kraft-brown: #8e604a;
    --kraft-dark: #6e4735;
    --ink-yellow: #e8cf1c;
    --ink-white: #ffffff;
    --stage: #d9dcdf;
  }
  * { margin: 0; padding: 0; box-sizing: border-box; }
  html, body { width: 1200px; height: 1000px; overflow: hidden; background: var(--stage); }
  .canvas { position: relative; width: 1200px; height: 1000px; }

  .lid {
    position: absolute; left: 220px; top: 30px; width: 760px; height: 760px;
    background: var(--kraft-brown); overflow: hidden;
    box-shadow: 0 8px 24px rgba(0,0,0,.18);
  }

  .sunburst {
    position: absolute; left: 0; top: 0; width: 100%; height: 570px;
    background: radial-gradient(circle at 50% 55%, #f0db3c 0%, var(--ink-yellow) 40%, #b99a2c 100%);
  }
  .pizza-lettering {
    position: absolute; left: 50%; top: 36px; transform: translateX(-50%);
    width: 380px; height: 130px; border-radius: 10px;
    background: linear-gradient(180deg, #ffffff, #e9e2dc);
  }
  .brand-seal {
    position: absolute; left: 50%; top: 190px; transform: translateX(-50%);
    width: 330px; height: 330px; border-radius: 50%; background: var(--ink-white);
    display: flex; flex-direction: column; align-items: center; justify-content: center; gap: 14px;
  }
  .brand-seal .seal-dot { width: 26px; height: 26px; border-radius: 50%; background: var(--kraft-brown); }
  .brand-name {
    font-family: "Archivo Black", sans-serif; color: var(--kraft-brown);
    font-size: 30px; line-height: 1.15; text-align: center; text-transform: uppercase;
  }

  .lid-footer {
    position: absolute; left: 0; top: 570px; width: 100%; height: 190px;
    display: grid; grid-template-columns: 1fr auto 1fr; align-items: center; column-gap: 24px;
    padding: 0 36px;
  }
  .contact-block { color: var(--ink-white); font-family: "Archivo Black", sans-serif; white-space: nowrap; }
  .contact-block .phone { font-size: 48px; line-height: 1; letter-spacing: 1px; }
  .contact-block .address { font-size: 21px; line-height: 1.2; margin-top: 10px; }
  .footer-mark {
    width: 110px; height: 62px; border-radius: 6px;
    background: linear-gradient(180deg, #ffffff, #ece6e0);
  }
  .web-address {
    color: var(--ink-yellow); font-family: "Roboto Condensed", sans-serif;
    font-weight: 700; font-size: 28px; white-space: nowrap;
  }
  .lid-footer .web-address { justify-self: end; }

  .side-panel {
    position: absolute; left: 220px; top: 820px; width: 760px; height: 140px;
    background: var(--kraft-brown);
    display: flex; align-items: center; justify-content: space-between; padding: 0 40px;
    box-shadow: 0 8px 24px rgba(0,0,0,.18);
  }
  .side-address { color: var(--ink-white); font-family: "Archivo Black", sans-serif; font-size: 20px; line-height: 1.25; white-space: nowrap; }
  .side-brand { display: flex; align-items: center; gap: 10px; }
  .side-brand .seal-dot { width: 16px; height: 16px; border-radius: 50%; background: var(--ink-yellow); }
  .side-brand .name { font-family: "Archivo Black", sans-serif; color: var(--ink-yellow); font-size: 18px; text-transform: uppercase; white-space: nowrap; }
  .side-contact { text-align: right; }
  .side-contact .phone { color: var(--ink-white); font-family: "Archivo Black", sans-serif; font-size: 38px; line-height: 1; white-space: nowrap; }
  .side-contact .web-address { font-size: 22px; }
</style>
</head>
<body>
<div class="canvas">
  <section class="lid">
    <div class="sunburst" role="img" aria-label="Yellow and brown sunburst rays radiating from the centre">
      <div class="pizza-lettering" role="img" aria-label="Large white script 'Pizza' hand lettering"></div>
      <div class="brand-seal">
        <span class="seal-dot"></span>
        <div class="brand-name">Marlow's<br>Finchyard<br>Pizzeria</div>
      </div>
    </div>
    <footer class="lid-footer">
      <div class="contact-block">
        <div class="phone">555-0148</div>
        <div class="address">1742 Alder Street<br>Westbrook Plaza</div>
      </div>
      <div class="footer-mark" role="img" aria-label="Small script 'Pizza' lettering"></div>
      <div class="web-address">marlowsfinchyard.com</div>
    </footer>
  </section>

  <section class="side-panel">
    <div class="side-address">1742 Alder Street<br>Westbrook Plaza</div>
    <div class="side-brand"><span class="seal-dot"></span><span class="name">Marlow's Finchyard</span></div>
    <div class="side-contact">
      <div class="phone">555-0148</div>
      <div class="web-address">marlowsfinchyard.com</div>
    </div>
  </section>
</div>
</body>
</html>
```